Design few pages for professional development app

I need a website design for a prototype project. The goal of the project is to prototype a few basic screens for a professional development application.

The final design should be clean, modern, and appeal to a professional millenial clientele.The designs have been wireframed (see attached), and we'd like these wireframes converted to design files.

Here is the list of goals and tasks that correspond to the design: https://sheets.plorvane.com/tables/d/7qWmK84x9PLzn3oTcB2vEaRyhUDs-kfNJ52tqXyMHw/edit?usp=sharing

Number of Pages Required

5+ page

Font styles to use
Serif
Sans Serif

Colors

Designer to choose colors to be used in the design.

Requirements
Nice to have
• Uses Google Material Design, Bootstrap, or another framework

```html
<!DOCTYPE html>
<html lang="en">
<head>
<meta charset="utf-8">
<title>ClimbPath – Suggested Tasks</title>
<link href="https://fonts.googleapis.com/css2?family=Mulish:wght@200;400;600;700;800&display=swap" rel="stylesheet">
<style>
  :root {
    --panel-blue: #6483c0;
    --page-bg: #f3f6fb;
    --card-bg: #ffffff;
    --card-done-border: #dde3ec;
    --ink: #1d1d1f;
    --ink-muted: #9a9a9a;
    --accent-blue: #1e88ef;
    --accent-rose: #c45a80;
    --ring-track: #a3a3a3;
    --ring-progress: #b4f07e;
    --tooltip-bg: #555d6b;
    --white: #ffffff;
  }
  * { box-sizing: border-box; margin: 0; padding: 0; }
  html, body { width: 1200px; height: 675px; overflow: hidden; }
  body { font-family: "Mulish", Arial, sans-serif; background: var(--page-bg); position: relative; }

  .sidebar {
    position: absolute; left: 0; top: 0; width: 600px; height: 675px;
    background: var(--panel-blue); color: var(--white);
  }
  .brand { position: absolute; left: 28px; top: 17px; font-size: 13.5px; font-weight: 800; letter-spacing: .1px; }
  .search-icon { position: absolute; left: 455px; top: 18px; }
  .user-menu { position: absolute; left: 490px; top: 19px; font-size: 10.5px; font-weight: 700; display: flex; align-items: center; gap: 6px; }
  .greeting { position: absolute; left: 0; width: 600px; top: 232px; text-align: center; font-size: 21px; font-weight: 700; }
  .progress-ring { position: absolute; left: 200px; top: 291px; }
  .progress-count { position: absolute; left: 200px; top: 291px; width: 200px; height: 200px; text-align: center; }
  .progress-count .done { position: absolute; left: 62px; top: 52px; font-size: 56px; font-weight: 200; line-height: 1; }
  .progress-count .total { position: absolute; left: 104px; top: 91px; font-size: 20px; font-weight: 400; }
  .progress-count .label { position: absolute; left: 0; width: 178px; top: 125px; font-size: 9.5px; font-weight: 800; letter-spacing: .2px; }

  .task-list {
    position: absolute; left: 628px; top: 28px; width: 544px;
    list-style: none; display: flex; flex-direction: column; gap: 10.5px;
  }
  .task {
    position: relative; background: var(--card-bg); border-radius: 4px;
    height: 66.8px; padding-left: 49px; padding-right: 60px;
    display: flex; flex-direction: column; justify-content: center;
  }
  .task.tall { height: 81.7px; }
  .task.done { background: var(--page-bg); border: 1px solid var(--card-done-border); }
  .task-icon { position: absolute; left: 14px; top: 50%; transform: translateY(-50%); color: var(--ink); }
  .task.done .task-icon { color: var(--ink-muted); }
  .task-goal { font-size: 14px; font-weight: 800; color: var(--ink); letter-spacing: .1px; line-height: 1.3; }
  .task-goal .duration { font-size: 9.5px; font-weight: 700; color: var(--ink-muted); letter-spacing: 0; }
  .task-step { font-size: 12.5px; color: var(--ink); line-height: 1.25; }
  .task.done .task-goal, .task.done .task-step { color: var(--ink-muted); }
  .task-action { position: absolute; left: 502px; top: 50%; transform: translateY(-50%); width: 28px; height: 28px; }

  .tooltip {
    position: absolute; left: 1111px; top: 176px; width: 65px; height: 21px;
    background: var(--tooltip-bg); color: var(--white); border-radius: 3px;
    font-size: 9px; font-weight: 700; display: flex; align-items: center; justify-content: center;
  }
  .tooltip::after {
    content: ""; position: absolute; left: 28px; bottom: -4px;
    border-left: 4px solid transparent; border-right: 4px solid transparent; border-top: 4px solid var(--tooltip-bg);
  }
</style>
</head>
<body>
<svg width="0" height="0" style="position:absolute">
  <defs>
    <symbol id="icon-person" viewBox="0 0 26 26"><g fill="none" stroke="currentColor" stroke-width="1.2"><circle cx="13" cy="8" r="5"/><path d="M2 25v-3c0-4 4-7 11-7s11 3 11 7v3z"/></g></symbol>
    <symbol id="icon-badge" viewBox="0 0 26 28"><g fill="none" stroke="currentColor" stroke-width="1.2"><path d="M13 1l3 2.5 3.8-.6 1.2 3.7 3.5 1.6-.9 3.8 1.9 3.3-2.9 2.5-.1 3.9-3.8.5-2.2 3.2L13 22l-3.5 1.9-2.2-3.2-3.8-.5-.1-3.9L.5 14.3l1.9-3.3-.9-3.8L5 5.6l1.2-3.7 3.8.6z"/><circle cx="13" cy="12" r="4"/><path d="M7 20l-3 7 4-1.5 2 3 2.5-6M19 20l3 7-4-1.5-2 3-2.5-6"/></g></symbol>
    <symbol id="icon-globe" viewBox="0 0 28 28"><g fill="none" stroke="currentColor" stroke-width="1.2"><circle cx="14" cy="14" r="12.5"/><ellipse cx="14" cy="14" rx="5.5" ry="12.5"/><path d="M1.5 14h25M3.5 7.5h21M3.5 20.5h21M14 1.5v25"/></g></symbol>
    <symbol id="icon-bolt" viewBox="0 0 22 32"><path d="M8 1h10l-5 11h7L5 31l4-14H3z" fill="none" stroke="currentColor" stroke-width="1.2" stroke-linejoin="round"/></symbol>
    <symbol id="btn-play" viewBox="0 0 28 28"><path d="M11 8.5v11l9-5.5z" fill="#fff"/></symbol>
  </defs>
</svg>

<aside class="sidebar">
  <div class="brand">ClimbPath</div>
  <svg class="search-icon" width="16" height="16" viewBox="0 0 16 16"><circle cx="6.5" cy="6.5" r="5.3" fill="none" stroke="#fff" stroke-width="1.6"/><path d="M10.4 10.4l4.4 4.4" stroke="#fff" stroke-width="1.8" stroke-linecap="round"/></svg>
  <div class="user-menu">Nora Ellison <svg width="9" height="6" viewBox="0 0 9 6"><path d="M0 0h9L4.5 5.5z" fill="#fff"/></svg></div>
  <h1 class="greeting">Nora, here's your list of suggested tasks.</h1>
  <svg class="progress-ring" width="200" height="200" viewBox="0 0 200 200">
    <circle cx="100" cy="100" r="97" fill="none" stroke="var(--ring-track)" stroke-width="4.5"/>
    <path d="M100 3 A97 97 0 0 1 165.5 28.5" fill="none" stroke="var(--ring-progress)" stroke-width="4.5"/>
  </svg>
  <div class="progress-count">
    <span class="done">2</span><span class="total">/16</span>
    <span class="label">COMPLETED</span>
  </div>
</aside>

<ul class="task-list">
  <li class="task done">
    <svg class="task-icon" width="24" height="24"><use href="#icon-person"/></svg>
    <div class="task-goal">PERSONAL GROWTH <span class="duration">(30 min.)</span></div>
    <div class="task-step">Write your personal brand statement</div>
    <svg class="task-action" viewBox="0 0 28 28"><circle cx="14" cy="14" r="12.8" fill="none" stroke="var(--accent-blue)" stroke-width="1.8"/><path d="M8.5 14.3l3.8 3.8 7.5-8" fill="none" stroke="var(--accent-blue)" stroke-width="2.4" stroke-linecap="round" stroke-linejoin="round"/></svg>
  </li>
  <li class="task done">
    <svg class="task-icon" width="24" height="27"><use href="#icon-badge"/></svg>
    <div class="task-goal">GET A PROMOTION <span class="duration">(60 min.)</span></div>
    <div class="task-step">Have a career conversation with your manager</div>
    <svg class="task-action" viewBox="0 0 28 28"><circle cx="14" cy="14" r="12.8" fill="none" stroke="var(--accent-blue)" stroke-width="1.8"/><path d="M8.5 14.3l3.8 3.8 7.5-8" fill="none" stroke="var(--accent-blue)" stroke-width="2.4" stroke-linecap="round" stroke-linejoin="round"/></svg>
  </li>
  <li class="task">
    <svg class="task-icon" width="24" height="27"><use href="#icon-badge"/></svg>
    <div class="task-goal">GET A PROMOTION <span class="duration">(60 min.)</span></div>
    <div class="task-step">Ask for peer feedback</div>
    <svg class="task-action" viewBox="0 0 28 28"><circle cx="14" cy="14" r="14" fill="var(--accent-blue)"/><use href="#btn-play"/></svg>
  </li>
  <li class="task tall">
    <svg class="task-icon" width="25" height="25"><use href="#icon-globe"/></svg>
    <div class="task-goal">BUILD MY NETWORK <span class="duration">(30 min.)</span></div>
    <div class="task-step">Make a list of influential people in your field at your company, and outside of your company</div>
    <svg class="task-action" viewBox="0 0 28 28"><circle cx="14" cy="14" r="14" fill="var(--accent-rose)"/><use href="#btn-play"/></svg>
  </li>
  <li class="task">
    <svg class="task-icon" width="20" height="30"><use href="#icon-bolt"/></svg>
    <div class="task-goal">BE A BETTER LEADER</div>
    <div class="task-step">Have a career conversation with your direct report</div>
    <svg class="task-action" viewBox="0 0 28 28"><circle cx="14" cy="14" r="14" fill="var(--accent-rose)"/><use href="#btn-play"/></svg>
  </li>
  <li class="task">
    <svg class="task-icon" width="20" height="30"><use href="#icon-bolt"/></svg>
    <div class="task-goal">BE A BETTER LEADER</div>
    <div class="task-step">Solicit feedback from your direct reports</div>
    <svg class="task-action" viewBox="0 0 28 28"><circle cx="14" cy="14" r="14" fill="var(--accent-rose)"/><use href="#btn-play"/></svg>
  </li>
  <li class="task">
    <svg class="task-icon" width="20" height="30"><use href="#icon-bolt"/></svg>
    <div class="task-goal">BE A BETTER LEADER</div>
    <div class="task-step">Meet with your skip-level reports</div>
    <svg class="task-action" viewBox="0 0 28 28"><circle cx="14" cy="14" r="14" fill="var(--accent-rose)"/><use href="#btn-play"/></svg>
  </li>
  <li class="task">
    <svg class="task-icon" width="24" height="27"><use href="#icon-badge"/></svg>
    <div class="task-goal">GET A PROMOTION</div>
    <div class="task-step">Set up a career lunch with someone at a higher level besides your manager</div>
    <svg class="task-action" viewBox="0 0 28 28"><circle cx="14" cy="14" r="14" fill="var(--accent-rose)"/><use href="#btn-play"/></svg>
  </li>
  <li class="task"></li>
</ul>

<div class="tooltip">Start Task</div>
</body>
</html>
```